Halvex Consulting

Hi,
I have my own network consulting business (just me)
and need to get a logo and business card design together,

Based in New Zealand,

Gareth Pollard
Unified Communications and Network Architect

/design engineer,
and would like this to be the basis for personal branding and company identity

Reason: I will be off site for a couple of days - so you have some more time

Business

• I have the basis for a optional logo - needs color -

```html
<!DOCTYPE html>
<html lang="en">
<head>
<meta charset="utf-8">
<title>Halvex Consulting – Business Cards</title>
<link rel="stylesheet" href="https://fonts.googleapis.com/css2?family=Marcellus&family=Open+Sans:wght@400;600;700&display=swap">
<style>
  :root {
    --backdrop: #262626;
    --card-white: #fbfbfb;
    --cyan: #4fc3dc;
    --mid-blue: #3a8fc9;
    --indigo: #3b2a93;
    --name-blue: #1f78c1;
    --ink: #222222;
    --ink-soft: #3a3a3a;
    --white: #ffffff;
  }
  * { margin: 0; padding: 0; box-sizing: border-box; }
  html, body { width: 1200px; height: 892px; overflow: hidden; }
  body {
    background: var(--backdrop);
    position: relative;
    font-family: "Open Sans", Arial, sans-serif;
  }
  .card {
    position: absolute;
    width: 521px;
    height: 296px;
    border-radius: 20px;
    overflow: hidden;
    box-shadow: 0 4px 10px rgba(0,0,0,0.5);
  }
  .card--front {
    background:
      radial-gradient(ellipse 70% 90% at 38% 55%, rgba(120,215,235,0.9) 0%, rgba(70,170,215,0.6) 35%, rgba(59,42,147,0) 80%),
      linear-gradient(100deg, #5a7ccf 0%, var(--mid-blue) 40%, var(--indigo) 100%);
  }
  .card--front-logo { left: 74px; top: 120px; }
  .card--front-plain { left: 608px; top: 120px; }
  .front__decoration {
    position: absolute;
    left: 0; top: 0;
    width: 280px; height: 296px;
    background: radial-gradient(circle at 45% 60%, rgba(255,255,255,0.14), rgba(255,255,255,0) 70%);
  }
  .front__mark {
    position: absolute;
    left: 348px; top: 118px;
    width: 46px; height: 46px;
    border-radius: 50%;
    background: var(--white);
  }
  .front__identity {
    position: absolute;
    right: 30px; top: 238px;
    text-align: right;
    color: var(--white);
  }
  .front__company {
    font-family: "Marcellus", Georgia, serif;
    font-size: 26px;
    line-height: 1;
    letter-spacing: 0.3px;
  }
  .front__tagline {
    font-size: 12px;
    margin-top: 7px;
  }
  .card--back {
    left: 77px; top: 459px;
    background: var(--card-white);
  }
  .back__band {
    position: absolute;
    left: 0; bottom: 0;
    width: 100%; height: 31px;
    background: linear-gradient(90deg, #5aa8d8 0%, var(--cyan) 25%, #4a86c8 60%, var(--indigo) 100%);
  }
  .back__brand {
    position: absolute;
    left: 24px; top: 92px;
    width: 196px;
    text-align: center;
  }
  .back__mark {
    width: 46px; height: 46px;
    border-radius: 50%;
    background: var(--mid-blue);
    margin: 0 auto 40px;
  }
  .back__company {
    font-family: "Marcellus", Georgia, serif;
    font-size: 17.5px;
    color: var(--ink);
    line-height: 1;
  }
  .back__tagline {
    font-size: 8px;
    color: var(--ink);
    margin-top: 4px;
  }
  .back__person {
    position: absolute;
    left: 272px; top: 42px;
  }
  .back__name {
    font-size: 17.5px;
    font-weight: 700;
    color: var(--name-blue);
    line-height: 1.2;
  }
  .back__role {
    font-size: 14px;
    color: var(--ink-soft);
    line-height: 1.35;
  }
  .back__address {
    position: absolute;
    left: 273px; top: 148px;
    font-size: 13px;
    color: var(--ink-soft);
  }
  .back__contacts {
    position: absolute;
    left: 273px; top: 190px;
    list-style: none;
    font-size: 13px;
    color: var(--ink-soft);
  }
  .back__contacts li {
    display: flex;
    align-items: center;
    height: 19px;
  }
  .back__contacts svg {
    width: 12px; height: 12px;
    margin-right: 7px;
    fill: var(--name-blue);
    flex: none;
  }
</style>
</head>
<body>

<section class="card card--front card--front-logo">
  <div class="front__decoration"></div>
  <div class="front__mark"></div>
  <div class="front__identity">
    <p class="front__company">HALVEX CONSULTING</p>
    <p class="front__tagline">Unified Communications and Network Architect</p>
  </div>
</section>

<section class="card card--front card--front-plain">
  <div class="front__decoration"></div>
  <div class="front__identity">
    <p class="front__company">HALVEX CONSULTING</p>
    <p class="front__tagline">Unified Communications and Network Architect</p>
  </div>
</section>

<section class="card card--back">
  <div class="back__brand">
    <div class="back__mark"></div>
    <p class="back__company">HALVEX CONSULTING</p>
    <p class="back__tagline">Unified Communications and Network Architect</p>
  </div>

  <div class="back__person">
    <p class="back__name">Gareth Pollard</p>
    <p class="back__role">Design Engineer</p>
  </div>

  <p class="back__address">Wellington 6011 New Zealand</p>

  <ul class="back__contacts">
    <li>
      <svg viewBox="0 0 12 12" aria-hidden="true"><path d="M1 4c0-2 2-3 5-3s5 1 5 3v1H8V4H4v1H1z"/><rect x="2" y="6" width="8" height="5" rx="1"/></svg>
      021 555 0147
    </li>
    <li>
      <svg viewBox="0 0 12 12" aria-hidden="true"><rect x="1" y="8" width="2" height="3"/><rect x="4" y="6" width="2" height="5"/><rect x="7" y="4" width="2" height="7"/><rect x="10" y="1" width="2" height="10"/></svg>
      021 555 0147
    </li>
    <li>
      <svg viewBox="0 0 12 12" aria-hidden="true"><path d="M1 3h10v7H1z" fill="none" stroke="#1f78c1" stroke-width="1"/><path d="M1 3l5 4 5-4" fill="none" stroke="#1f78c1" stroke-width="1"/></svg>
      gareth@halvexconsulting.com
    </li>
    <li>
      <svg viewBox="0 0 12 12" aria-hidden="true"><circle cx="6" cy="6" r="5"/><path d="M1 6h10M6 1v10M3 2.5c2 2 2 5 0 7M9 2.5c-2 2-2 5 0 7" fill="none" stroke="#fbfbfb" stroke-width="0.8"/></svg>
      www.halvexconsulting.com
    </li>
  </ul>

  <div class="back__band"></div>
</section>

</body>
</html>
```